CASH PAYMENT DISCOUNT NOTICE POSTED IN CASH REGISTER AREA

LOOKING TO MAKE A FLYER OR A POSTED NOTICE FOR CUSTOMERS PAYING FOR OVER-THE-COUNTER MERCHANDISE AND WHO PAY BY CASH METHOD TO GET A 4% CASH DISCOUNT.
PRESCRIPTIONS ARE EXCLUDED FROM THIS CASH DISCOUNT.

Target Market(s)

RETAIL CUSTOMERS

Industry/Entity Type

RETAIL PHARMACY

Colors
0054AA
0677BA
7BADD7
CADEEF
E8F1F8
EB3D1F
EC4F4E
F09395
F8D3D4
FCEDEE

Requirements
Must have
• LOGO COLORS
Nice to have
• EYE CATCHING

```html
<!DOCTYPE html>
<html lang="en">
<head>
<meta charset="utf-8">
<title>Cash Discount Notice</title>
<link rel="stylesheet" href="https://fonts.googleapis.com/css2?family=Montserrat:wght@400;700;800;900&family=Oswald:wght@600&display=swap">
<style>
  :root {
    --surround: #858685;
    --paper: #ffffff;
    --stone-light: #f5f5f5;
    --stone-mid: #dadada;
    --brand-blue: #2c55a6;
    --brand-blue-deep: #213f86;
    --brand-red: #b01e24;
    --ink-white: #ffffff;
  }
  html, body {
    margin: 0;
    width: 965px;
    height: 1200px;
    overflow: hidden;
    background: var(--surround);
    font-family: "Montserrat", sans-serif;
  }
  .notice-card {
    position: absolute;
    left: 82px;
    top: 82px;
    width: 800px;
    height: 1035px;
    background: var(--paper);
    box-shadow: 6px 8px 10px rgba(0,0,0,0.35);
    overflow: hidden;
  }
  .card-backdrop { position: absolute; inset: 0; }
  .brand {
    position: absolute;
    top: 68px;
    left: 0;
    width: 800px;
    display: flex;
    justify-content: center;
    align-items: center;
    gap: 16px;
  }
  .brand-mark { width: 34px; height: 34px; background: var(--brand-blue); }
  .brand-name {
    font-weight: 700;
    font-size: 44px;
    letter-spacing: 2px;
    color: var(--brand-red);
    line-height: 1;
  }
  .notice-tag {
    position: absolute;
    left: 236px;
    top: 178px;
    width: 329px;
    height: 72px;
    display: flex;
    align-items: center;
    justify-content: center;
    color: var(--ink-white);
    font-weight: 900;
    font-size: 52px;
    letter-spacing: 1px;
  }
  .headline {
    position: absolute;
    left: 0;
    width: 800px;
    text-align: center;
    margin: 0;
    line-height: 1;
    font-weight: 400;
  }
  .headline strong { font-weight: 900; }
  .headline-pay { top: 290px; font-size: 70px; color: var(--brand-blue); }
  .headline-cash { top: 358px; font-size: 70px; color: var(--brand-red); letter-spacing: -1px; }
  .headline-to {
    position: absolute;
    left: 308px;
    top: 422px;
    margin: 0;
    font-size: 64px;
    font-weight: 400;
    color: var(--brand-blue);
    line-height: 1;
  }
  .thumb-art {
    position: absolute;
    left: 181px;
    top: 496px;
    width: 452px;
    height: 364px;
  }
  .discount-text {
    position: absolute;
    left: 318px;
    top: 600px;
    width: 300px;
    transform: rotate(-8deg) skewX(-8deg);
    transform-origin: left top;
    font-family: "Oswald", sans-serif;
    font-weight: 600;
    color: var(--ink-white);
    line-height: 1;
  }
  .discount-text .line-get { display: block; font-size: 50px; }
  .discount-text .line-get b { font-size: 80px; font-weight: 600; }
  .discount-text .line-word { display: block; font-size: 64px; margin-top: -8px; }
  .footer-note {
    position: absolute;
    left: 0;
    width: 800px;
    margin: 0;
    text-align: center;
    color: var(--ink-white);
    line-height: 1;
    white-space: nowrap;
  }
  .footer-title { top: 925px; font-size: 31px; font-weight: 700; }
  .footer-line { top: 970px; font-size: 33px; font-weight: 400; }
  .footer-line strong { font-weight: 700; }
</style>
</head>
<body>
  <main class="notice-card">
    <svg class="card-backdrop" width="800" height="1035" viewBox="0 0 800 1035">
      <defs>
        <radialGradient id="stoneFill" cx="50%" cy="45%" r="70%">
          <stop offset="0" stop-color="var(--stone-light)"/>
          <stop offset="1" stop-color="var(--stone-mid)"/>
        </radialGradient>
      </defs>
      <path d="M0 175 Q400 250 800 175 L800 1035 L0 1035 Z" fill="url(#stoneFill)"/>
      <path d="M0 175 Q400 250 800 175" fill="none" stroke="var(--brand-red)" stroke-width="6"/>
      <polygon points="256,178 565,178 545,250 236,250" fill="var(--brand-red)"/>
      <path d="M0 945 Q400 850 800 945 L800 1035 L0 1035 Z" fill="var(--brand-red)"/>
      <path d="M0 953 Q400 862 800 953 L800 1035 L0 1035 Z" fill="var(--brand-blue)"/>
    </svg>

    <header class="brand">
      <span class="brand-mark"></span>
      <span class="brand-name">Meridian Pharmacy</span>
    </header>

    <div class="notice-tag">NOTICE</div>

    <p class="headline headline-pay"><strong>PAY</strong> BY</p>
    <p class="headline headline-cash"><strong>CASH</strong> METHOD</p>
    <p class="headline-to">TO</p>

    <svg class="thumb-art" role="img" aria-label="Illustration of a blue thumbs-up hand with a gold dollar coin and a yellow upward arrow" viewBox="0 0 452 364">
      <defs>
        <linearGradient id="thumbFill" x1="0" y1="0" x2="1" y2="1">
          <stop offset="0" stop-color="var(--brand-blue)"/>
          <stop offset="1" stop-color="var(--brand-blue-deep)"/>
        </linearGradient>
      </defs>
      <rect x="0" y="0" width="452" height="364" rx="28" fill="url(#thumbFill)"/>
    </svg>

    <div class="discount-text">
      <span class="line-get">GET A <b>4%</b></span>
      <span class="line-word">DISCOUNT</span>
    </div>

    <p class="footer-note footer-title">Prescriptions</p>
    <p class="footer-note footer-line">Are <strong>Excluded</strong> From This <strong>Cash Discount</strong></p>
  </main>
</body>
</html>
```